UI design for Fast Food Restaurant Self-Order App

Background:
App purpose: for fast food restaurant customers to self order food/drink by choosing item image, and make payment by tapping the credit card on the card terminal.
Reference: https://www.brivalotech.example/product-overview/self-order-kiosks/
Attachment:
Wireframes. (wire frames provide general idea and the information to display, they are not a strict guideline for layout design.)
Pollardo's Self ordering app.
Intro:
We have built a (for restaurant and cafe) Self Ordering and Payment app, similar to Pollardo's self ordering software in most of their new restaurants. Our app will be placed in a Quorvex Panes 10 OS touch screen Kiosk(screen size 4:3 or Portrait 16:9) within the restaurant/cafe premise.
Pages to be designed:
Page 1. Food Browsing Page. displays all food images(to be provided by cafes) by categories, and displays the Cart. This page will lead to Page 2 or Page 3.
'Cart' section should include:
'cart items/selected items', its quantity and price. like Pollardos' app.
When click on a Cart Item, we need to allow to change quantity or 'change Choice'. The UI handling these change requests with ease will be one deciding factor for us to choose your design.
Fact: up to 10 food categories, and 10 - 25 food items under each categories.
When click on one item image, it goes to Page 2.
Page 2. Item Detail/Description Page. Shows description of the food, and its available Choice(other food items or Special Request, up to 12) will also be displayed. 'Add item to cart' action(Button Name: ADD) will happen here and go back to Browsing Page 1.
e.g. Item 'Fried Rice' Page. the Choice could be 'Add Egg', 'Add Meat', 'No Chilli' etc.
Page 3. Order Review Page. No edit features allowed on this page, only two buttons: 'No' to go back to Browsing Page, or 'Yes' to proceed to Payment Page 4. Check Pollardo's screen.
Page 4. Payment Page - Prompt user to Insert or Tap credit card on the credit card terminal. (Exact wording: PLEASE FOLLOW INSTRUCTIONS DISPLAYED ON CREDIT CARD TERMINAL BELOW)
Page 5. Payment status. Successful / Failed.
Our considerations to pick the winner:
1. In terms of design for this task, we look out for page layout, effects, fonts, button style and overall colour scheme. the design should present itself in a clean and modern look, with minimum clicking or scrolling. The app aims to help customers choose and pay for their items quickly.
2.we need to handle both 4:3(as shown in wire frames) and 16:9 screens(like Pollardo's). there will be a lot more vertical space to utilise when it is in 16:9, resulting less scrolling than 4:3. tell us what you think.
All questions are welcome.
Winner has opportunity to work on a few more app UI. Cheers!
Industry/Entity Type
Fast Food Restaurant
Requirements
Must have
- Button colour differentiation - helps people know what to click next.
- best use of screen space. minimum click and scrolls.
Nice to have
- any personal touch.
Should not have
- unrelated design pattern, e.g. a cute animal or flower pattern in the layout.

```html
<!DOCTYPE html>
<html lang="en">
<head>
<meta charset="utf-8">
<title>Self-Order Kiosk – Item Detail</title>
<link rel="stylesheet" href="https://fonts.googleapis.com/css2?family=Baloo+2:wght@500;600;700;800&family=Quicksand:wght@500;600;700&family=Nunito:wght@500;700;800&display=swap">
<style>
  :root{
    --orange:#f26a30;
    --orange-light:#f9a56e;
    --ink:#1e1e1e;
    --muted:#555;
    --price-red:#d01818;
    --line:#d8d8d8;
    --grey-band:#efefef;
    --dark-btn:#2f2f2f;
    --yellow:#f9c510;
    --green:#14c43e;
    --red:#d8201f;
    --white:#ffffff;
  }
  *{box-sizing:border-box;margin:0;padding:0}
  html,body{width:1200px;height:960px;overflow:hidden;background:var(--white)}
  body{position:relative;font-family:"Quicksand",sans-serif;color:var(--ink)}
  .abs{position:absolute}

  /* sidebar */
  .brand-badge{left:38px;top:33px;width:100px;height:100px;border-radius:50%;
    background:radial-gradient(circle,#f47a3e 0 58%,#fff 59% 64%,#f47a3e 65%);}
  .category{left:26px;width:124px;height:132px;border:1.5px solid #bdbdbd;border-radius:8px;background:#fff;
    display:flex;flex-direction:column;align-items:center;justify-content:flex-end;padding-bottom:8px;
    font-family:"Baloo 2",sans-serif;font-weight:600;font-size:15px}
  .category .thumb{width:86px;height:70px;border-radius:10px;margin-bottom:10px}
  .category.is-active{border-color:transparent;color:var(--orange);font-weight:800}

  /* header */
  .section-bar{left:200px;top:17px;width:1000px;height:52px;border-radius:26px 0 0 26px;
    background:linear-gradient(180deg,var(--orange-light),var(--orange));
    color:#fff;font-family:"Baloo 2",sans-serif;font-weight:700;font-size:21px;padding:10px 0 0 28px}

  .back-btn{left:761px;top:96px;width:82px;height:33px;border-radius:17px;background:linear-gradient(#4a4a4a,#1c1c1c);
    color:#fff;font-family:"Baloo 2",sans-serif;font-weight:700;font-size:17px;text-align:center;line-height:35px}

  .dish-photo{left:208px;top:142px;width:212px;height:158px;border-radius:45% 50% 42% 48%;
    background:radial-gradient(ellipse at 45% 45%,#8a3a2a,#5b2418 70%,#fff 72%)}
  .dish-title{left:467px;top:160px;font-family:"Baloo 2",sans-serif;font-weight:700;font-size:18px}
  .dish-desc{left:467px;top:199px;width:362px;font-size:14.5px;line-height:22.5px;color:#333;font-weight:500}
  .dish-price{left:467px;top:296px;color:var(--price-red);font-weight:700;font-size:16px}

  .price-box{left:200px;top:391px;width:643px;height:77px;border:1.5px solid #bfbfbf;border-radius:39px}
  .price-label{left:38px;top:18px;font-family:"Nunito",sans-serif;font-size:28px;font-weight:500;color:#333}
  .price-value{left:140px;top:16px;font-family:"Nunito",sans-serif;font-size:30px;font-weight:800;color:var(--price-red)}
  .round-btn{width:52px;height:52px;border-radius:50%;background:radial-gradient(circle at 40% 35%,#555,#1a1a1a);
    top:11px;box-shadow:0 2px 3px rgba(0,0,0,.3)}
  .round-btn.minus{left:406px}
  .round-btn.plus{left:582px}
  .qty-label{left:479px;top:5px;width:80px;text-align:center;font-family:"Nunito",sans-serif;font-weight:700;font-size:13.5px;letter-spacing:.5px}
  .qty-value{left:479px;top:27px;width:80px;text-align:center;font-family:"Baloo 2",sans-serif;font-weight:600;font-size:28px}

  .addons-title{left:200px;top:542px;font-family:"Baloo 2",sans-serif;font-weight:700;font-size:18px}
  .addon{width:140px;text-align:center;top:609px}
  .addon .thumb{width:84px;height:58px;margin:0 auto;border-radius:12px}
  .addon .name{font-family:"Baloo 2",sans-serif;font-weight:600;font-size:14.5px;margin-top:14px}
  .stepper{display:flex;height:33px;border-radius:3px;overflow:hidden;box-shadow:0 1px 3px rgba(0,0,0,.35)}
  .stepper .step{width:32px;background:linear-gradient(#444,#1c1c1c);display:flex;align-items:center;justify-content:center}
  .stepper .count{flex:1;background:#fff;text-align:center;font-family:"Nunito",sans-serif;font-size:20px;line-height:33px;border-top:1px solid #333;border-bottom:1px solid #333}
  .addon .stepper{width:100px;margin:14px auto 0}
  .scroll-track{left:220px;top:793px;width:603px;height:9px;border-radius:5px;background:#ececec}
  .scroll-thumb{left:80px;top:0;width:125px;height:9px;border-radius:5px;background:#d6d6d6}

  .add-cart-btn{left:409px;top:854px;width:224px;height:65px;border-radius:33px;background:linear-gradient(#ffd21a,#f4b400);
    color:#fff;font-family:"Baloo 2",sans-serif;font-weight:800;font-size:23px;letter-spacing:1px;text-align:center;line-height:68px;
    box-shadow:0 3px 6px rgba(0,0,0,.15)}

  /* orders panel */
  .orders{left:881px;top:36px;width:300px;height:905px;background:#fff;box-shadow:-2px 3px 8px rgba(0,0,0,.18)}
  .orders-title{left:18px;top:17px;font-family:"Baloo 2",sans-serif;font-weight:700;font-size:19px}
  .orders-hint{left:18px;top:53px;font-size:10.5px;color:#444;font-weight:600}
  .orders-rule{left:18px;top:84px;width:264px;height:1px;background:var(--line)}
  .row{left:0;width:300px;height:38px;font-family:"Baloo 2",sans-serif;font-weight:600;font-size:14px}
  .row span{position:absolute;top:9px}
  .row .item{left:18px}
  .row .qty{left:204px;width:10px;text-align:center}
  .row .amt{right:18px;color:var(--price-red);font-family:"Nunito",sans-serif}
  .row.head{font-weight:700}
  .row.head .qty{left:194px;width:30px}
  .row.head .amt{color:var(--ink);font-family:"Baloo 2",sans-serif}
  .row.shaded{background:#f6f6f6}
  .editing{left:0;top:229px;width:300px;height:130px}
  .pill{height:30px;border-radius:15px;color:#fff;font-family:"Baloo 2",sans-serif;font-weight:700;font-size:14px;text-align:center;line-height:32px;box-shadow:0 2px 3px rgba(0,0,0,.2)}
  .pill.remove{left:13px;top:68px;width:75px;background:linear-gradient(#ea3a36,#c81c1c)}
  .pill.change{left:104px;top:68px;width:75px;background:linear-gradient(#fccf2e,#f2b400)}
  .editing .stepper{position:absolute;left:195px;top:68px;width:92px;height:30px}
  .editing .stepper .step{width:28px}
  .editing .stepper .count{font-size:16px;line-height:28px}
  .tally-rule{left:18px;top:437px;width:264px;border-top:2px dashed #888;height:6px;border-bottom:2px dashed #888}
  .total{left:18px;top:480px;font-family:"Baloo 2",sans-serif;font-weight:800;font-size:23px}
  .total-amt{right:18px;top:480px;font-family:"Nunito",sans-serif;font-weight:800;font-size:23px;color:var(--price-red)}
  .big-btn{left:19px;width:262px;height:53px;border-radius:27px;color:#fff;font-family:"Baloo 2",sans-serif;font-weight:800;
    font-size:23px;letter-spacing:1.5px;text-align:center;line-height:57px;box-shadow:0 3px 5px rgba(0,0,0,.2)}
  .big-btn.order{top:758px;background:linear-gradient(#2ee04f,#0fae33)}
  .big-btn.cancel{top:831px;background:linear-gradient(#ee3b36,#be1515)}
</style>
</head>
<body>

<aside>
  <div class="abs brand-badge" role="img" aria-label="Restaurant emblem with spoon and fork"></div>
  <div class="abs category" style="top:163px"><div class="thumb" role="img" aria-label="Christmas dish photo" style="background:linear-gradient(135deg,#d8262c,#f1c24a)"></div>Christmas</div>
  <div class="abs category" style="top:322px"><div class="thumb" role="img" aria-label="Mini cakes photo" style="background:linear-gradient(135deg,#6b2a1c,#e9a53a)"></div>Mini Cakes</div>
  <div class="abs category" style="top:482px"><div class="thumb" role="img" aria-label="Whole cake photo" style="background:linear-gradient(135deg,#7a4a2a,#e8d8c8)"></div>Whole Cakes</div>
  <div class="abs category is-active" style="top:640px"><div class="thumb" role="img" aria-label="Main course photo" style="background:linear-gradient(135deg,#b8543a,#e6c15a)"></div>Main Menu</div>
  <div class="abs category" style="top:801px"><div class="thumb" role="img" aria-label="Add-on ingredients photo" style="background:linear-gradient(135deg,#e8e2d6,#d08a3a)"></div>Add Ons</div>
</aside>

<main>
  <div class="abs section-bar">Main Menu</div>
  <div class="abs back-btn">Back</div>

  <div class="abs dish-photo" role="img" aria-label="Grilled beef steak with peppers"></div>
  <h1 class="abs dish-title">Beauty and the Beef</h1>
  <p class="abs dish-desc">Topped with sautéed onions and mushrooms, with a starchy side dish; usually baked or mashed potatoes, or thick cut french fries known as steak fries.</p>
  <div class="abs dish-price">$12.49</div>

  <div class="abs price-box">
    <span class="abs price-label">Price:</span>
    <span class="abs price-value">$ 37.47</span>
    <div class="abs round-btn minus"><svg width="52" height="52"><rect x="13" y="24" width="26" height="4" fill="#fff"/></svg></div>
    <span class="abs qty-label">QUANTITY</span>
    <span class="abs qty-value">3</span>
    <div class="abs round-btn plus"><svg width="52" height="52"><rect x="13" y="24" width="26" height="4" fill="#fff"/><rect x="24" y="13" width="4" height="26" fill="#fff"/></svg></div>
  </div>

  <h2 class="abs addons-title">Add Ons</h2>
  <svg class="abs" style="left:200px;top:656px" width="16" height="42"><polyline points="13,2 3,21 13,40" fill="none" stroke="#999" stroke-width="1.5"/></svg>
  <svg class="abs" style="left:826px;top:656px" width="16" height="42"><polyline points="3,2 13,21 3,40" fill="none" stroke="#999" stroke-width="1.5"/></svg>

  <div class="abs addon" style="left:212px"><div class="thumb" role="img" aria-label="French fries" style="background:linear-gradient(#f7c640,#e59a1c)"></div><div class="name">Fries</div>
    <div class="stepper"><div class="step"><svg width="14" height="14"><rect y="6" width="14" height="2.5" fill="#fff"/></svg></div><div class="count">0</div><div class="step"><svg width="14" height="14"><rect y="6" width="14" height="2.5" fill="#fff"/><rect x="5.8" width="2.5" height="14" fill="#fff"/></svg></div></div></div>
  <div class="abs addon" style="left:371px"><div class="thumb" role="img" aria-label="Mushrooms" style="background:linear-gradient(#e8dccb,#b89c7c)"></div><div class="name">Mushrooms</div>
    <div class="stepper"><div class="step"><svg width="14" height="14"><rect y="6" width="14" height="2.5" fill="#fff"/></svg></div><div class="count">0</div><div class="step"><svg width="14" height="14"><rect y="6" width="14" height="2.5" fill="#fff"/><rect x="5.8" width="2.5" height="14" fill="#fff"/></svg></div></div></div>
  <div class="abs addon" style="left:531px"><div class="thumb" role="img" aria-label="Red onions" style="background:linear-gradient(#a8283a,#5c1020)"></div><div class="name">Onions</div>
    <div class="stepper"><div class="step"><svg width="14" height="14"><rect y="6" width="14" height="2.5" fill="#fff"/></svg></div><div class="count">0</div><div class="step"><svg width="14" height="14"><rect y="6" width="14" height="2.5" fill="#fff"/><rect x="5.8" width="2.5" height="14" fill="#fff"/></svg></div></div></div>
  <div class="abs addon" style="left:690px"><div class="thumb" role="img" aria-label="Fresh parsley" style="background:linear-gradient(#4cae3a,#1f6a1a)"></div><div class="name">Parsley</div>
    <div class="stepper"><div class="step"><svg width="14" height="14"><rect y="6" width="14" height="2.5" fill="#fff"/></svg></div><div class="count">0</div><div class="step"><svg width="14" height="14"><rect y="6" width="14" height="2.5" fill="#fff"/><rect x="5.8" width="2.5" height="14" fill="#fff"/></svg></div></div></div>

  <div class="abs scroll-track"><div class="abs scroll-thumb"></div></div>
  <div class="abs add-cart-btn">ADD TO CART</div>
</main>

<section class="abs orders">
  <h2 class="abs orders-title">Your Orders</h2>
  <p class="abs orders-hint">Tap an item to change or remove</p>
  <div class="abs orders-rule"></div>

  <div class="abs row head" style="top:102px"><span class="item">Item</span><span class="qty">Qty</span><span class="amt">Price</span></div>
  <div class="abs row shaded" style="top:138px"><span class="item">Steaks on a Plane</span><span class="qty">1</span><span class="amt">10.30</span></div>
  <div class="abs row" style="top:178px"><span class="item">Roastbusters</span><span class="qty">1</span><span class="amt">20.00</span></div>

  <div class="abs editing">
    <svg class="abs" style="left:0;top:0" width="300" height="130">
      <polygon fill="var(--grey-band)" points="0,12 12,0 24,12 36,0 48,12 60,0 72,12 84,0 96,12 108,0 120,12 132,0 144,12 156,0 168,12 180,0 192,12 204,0 216,12 228,0 240,12 252,0 264,12 276,0 288,12 300,0 300,130 288,118 276,130 264,118 252,130 240,118 228,130 216,118 204,130 192,118 180,130 168,118 156,130 144,118 132,130 120,118 108,130 96,118 84,130 72,118 60,130 48,118 36,130 24,118 12,130 0,118"/>
    </svg>
    <div class="abs row" style="top:24px"><span class="item">Jurassic Pork</span><span class="amt">18.40</span></div>
    <div class="abs pill remove">Remove</div>
    <div class="abs pill change">Change</div>
    <div class="stepper"><div class="step"><svg width="12" height="12"><rect y="5" width="12" height="2.5" fill="#fff"/></svg></div><div class="count">2</div><div class="step"><svg width="12" height="12"><rect y="5" width="12" height="2.5" fill="#fff"/><rect x="4.8" width="2.5" height="12" fill="#fff"/></svg></div></div>
  </div>

  <div class="abs row" style="top:388px"><span class="item">The Maiz Runner</span><span class="qty">2</span><span class="amt">7.00</span></div>
  <div class="abs tally-rule"></div>
  <div class="abs total">Total</div>
  <div class="abs total-amt">$55.70</div>

  <div class="abs big-btn order">ORDER</div>
  <div class="abs big-btn cancel">CANCEL</div>
</section>

</body>
</html>
```